Quillmarsh Property Solutions need a business card design

Hello guys. We would need a business card design asap please.
We are a start up property investment business based in London UK specialised in buying, selling, managing and letting properties and helping distressed property owners.
The name of our Business is Quillmarsh, the logo symbolises the four fundamental elements of the world (earth, air, fire and water) and so it stands for strength, stability, longevity.
We would like the business card to communicate professionalism and reliability. Many many thanks indeed for your work.

Details:

1.) Rosalind Opaleye
Property Investor
Mobile: +44(0)7700361752
Email: rosalind.quillmarsh@brindlepost.co.uk

2.) Anselm Opaleye
Property Investor
Mobile: +44(0)7700584029
Email: anselm.quillmarsh@brindlepost.co.uk

Investment

```html
<!DOCTYPE html>
<html lang="en">
<head>
<meta charset="utf-8">
<title>Quillmarsh Property Solutions – Business Card</title>
<link rel="stylesheet" href="https://fonts.googleapis.com/css2?family=Outfit:wght@700&family=Exo+2:wght@500&family=Tinos&family=Fondamento&display=swap">
<style>
  :root {
    --canvas: #ffffff;
    --card-white: #ffffff;
    --card-edge: #d8d8d8;
    --gold-light: #f7e600;
    --gold-mid: #ecd200;
    --gold-dark: #cfa90c;
    --ink: #111111;
    --ink-soft: #2a2a2a;
    --mark-dark: #1a1a1a;
    --mark-light: #ffffff;
    --text-shadow: rgba(60, 45, 0, 0.55);
  }
  * { margin: 0; padding: 0; box-sizing: border-box; }
  html, body {
    width: 1010px; height: 1200px; overflow: hidden;
    background: var(--canvas);
  }
  .canvas { position: relative; width: 1010px; height: 1200px; }

  .card {
    position: absolute;
    border-radius: 40px;
    overflow: hidden;
    border: 1px solid var(--card-edge);
  }
  .gold-surface {
    background: radial-gradient(ellipse at 50% 55%, var(--gold-light) 0%, var(--gold-mid) 45%, var(--gold-dark) 100%);
  }

  /* Front card */
  .card-front { left: 2px; top: 2px; width: 990px; height: 578px; background: var(--card-white); }
  .card-front .gold-band { position: absolute; left: 0; top: 403px; width: 100%; height: 175px; }

  .brand {
    position: absolute;
    display: flex; flex-direction: column; align-items: center;
    font-family: "Outfit", sans-serif; font-weight: 700;
    text-transform: uppercase; line-height: 1;
  }
  .brand-dot { border-radius: 50%; }
  .brand-name { letter-spacing: 0.02em; }
  .brand-tagline { letter-spacing: 0.02em; }

  .brand-hero { left: 0; width: 100%; top: 88px; color: var(--mark-dark); }
  .brand-hero .brand-dot { width: 96px; height: 96px; background: var(--mark-dark); margin-bottom: 110px; }
  .brand-hero .brand-name { font-size: 44px; }
  .brand-hero .brand-tagline { font-size: 19px; margin-top: 10px; }

  .brand-band { left: 0; width: 100%; top: 34px; color: var(--mark-light); }
  .brand-band .brand-dot { width: 48px; height: 48px; background: var(--mark-light); margin-bottom: 42px; }
  .brand-band .brand-name { font-size: 15px; }
  .brand-band .brand-tagline { font-size: 7px; margin-top: 4px; }

  /* Back card */
  .card-back { left: 10px; top: 608px; width: 990px; height: 580px; }
  .brand-corner { left: 22px; top: 40px; width: 230px; color: var(--mark-dark); }
  .brand-corner .brand-dot { width: 84px; height: 84px; background: var(--mark-dark); margin-bottom: 80px; }
  .brand-corner .brand-name { font-size: 25px; }
  .brand-corner .brand-tagline { font-size: 12px; margin-top: 8px; }

  .holder { position: absolute; right: 40px; top: 28px; text-align: right; }
  .holder-name { font-family: "Exo 2", sans-serif; font-weight: 500; font-size: 38px; color: var(--ink-soft); line-height: 1.1; }
  .holder-role { font-family: "Tinos", serif; font-size: 35px; color: var(--ink-soft); line-height: 1.1; }

  .contact-list { position: absolute; left: 148px; top: 242px; list-style: none; }
  .contact-item {
    font-family: "Fondamento", cursive; font-size: 40px; color: var(--ink-soft);
    line-height: 77px; white-space: nowrap;
    text-shadow: 1px 1px 1px var(--text-shadow);
  }
  .contact-item.email { font-size: 34px; }

  .website {
    position: absolute; left: 0; width: 100%; top: 500px; text-align: center;
    font-family: "Fondamento", cursive; font-size: 46px; color: var(--ink);
  }
</style>
</head>
<body>
<main class="canvas">
  <section class="card card-front" aria-label="Card front">
    <div class="brand brand-hero">
      <span class="brand-dot"></span>
      <span class="brand-name">Quillmarsh</span>
      <span class="brand-tagline">Property Solutions</span>
    </div>
    <div class="gold-band gold-surface">
      <div class="brand brand-band">
        <span class="brand-dot"></span>
        <span class="brand-name">Quillmarsh</span>
        <span class="brand-tagline">Property Solutions</span>
      </div>
    </div>
  </section>

  <section class="card card-back gold-surface" aria-label="Card back">
    <div class="brand brand-corner">
      <span class="brand-dot"></span>
      <span class="brand-name">Quillmarsh</span>
      <span class="brand-tagline">Property Solutions</span>
    </div>
    <div class="holder">
      <p class="holder-name">Rosalind Opaleye</p>
      <p class="holder-role">Property Investor</p>
    </div>
    <ul class="contact-list">
      <li class="contact-item">Company Address</li>
      <li class="contact-item">Mobile: +44(0)7700361752</li>
      <li class="contact-item email">Email: rosalind.quillmarsh@brindlepost.co.uk</li>
    </ul>
    <p class="website">Company Website</p>
  </section>
</main>
</body>
</html>
```